Website Design for Ridgeline Forgecraft And Decorative Steel LLC

Ridgeline Forgecraft & Decorative Steel is a veteran-owned and operated metal fabrication firm with decades of combined experience. We deliver custom, ornamental, and architectural metal solutions designed to meet the demands of commercial construction projects.

Our team specializes in fabricating and installing metal stairs, guardrails, handrails, railings, fencing, and ornamental metals that combined durability, code compliance, and visual appeal. We are a Small Business Enterprise (SBE), Veteran Business Enterprise (VBE), Service-Disabled Veteran-Owned Small Business (SDVOSB), and Veteran Friendly Business Enterprise (VFBE) Certified firm.

We are looking for a designer to create our website so that it can be used at our domain www.ridgelineforgecraftllc.example that we have sourced through Netplotter.example

We also have already created our corporate logo through crowdsource that can be incorporated into the web design.

Target Market(s)

General Contractors, Construction Managers, and Architects

Industry/Entity Type

Construction

Coding

Coded - Design and coding required

Number of Pages Required

5+ page

Requirements
Must have
• Company logo (Zip File Uploaded), About Us, Product Solutions, Target Market (See uploaded flyer)
Nice to have
• Patriotic Theme (American)
Should not have
• Web store

```html
<!DOCTYPE html>
<html lang="en">
<head>
<meta charset="utf-8">
<title>Ridgeline Forgecraft &amp; Decorative Steel</title>
<link href="https://fonts.googleapis.com/css2?family=Anton&family=Poppins:wght@400;500;600;700&display=swap" rel="stylesheet">
<style>
:root{
  --red:#c8102e;
  --red-dark:#a50d25;
  --navy:#0d2a6b;
  --navy-deep:#0a2259;
  --ink:#1b1b1b;
  --muted:#707070;
  --line:#e3e3e3;
  --field:#eeeeef;
  --canvas:#e4e4e4;
  --white:#ffffff;
}
*{box-sizing:border-box;margin:0;padding:0}
html,body{width:1200px;height:4691px;overflow:hidden}
body{background:var(--canvas);font-family:"Poppins",sans-serif;color:var(--ink)}
.page{position:absolute;left:47px;top:33px;width:1118px;height:4607px;background:var(--white);overflow:hidden}
.abs{position:absolute}
.heading{font-family:"Anton",sans-serif;font-weight:400;text-transform:uppercase;letter-spacing:.5px;line-height:1}
.red{color:var(--red)}
.btn{position:absolute;display:flex;align-items:center;justify-content:center;background:var(--red);color:var(--white);font-family:"Anton",sans-serif;text-transform:uppercase;font-size:12px;letter-spacing:.4px;border-radius:16px;height:28px}
.photo{position:absolute;border-radius:3px}

/* top bar + nav */
.topbar{left:0;top:0;width:1118px;height:22px;background:var(--navy);color:#fff;font-size:9px;display:flex;align-items:center;padding:0 141px}
.topbar span{margin-right:18px;display:flex;align-items:center;gap:5px}
.topbar .dot{width:6px;height:6px;border-radius:50%;background:var(--red)}
.topbar .socials{margin-left:auto;display:flex;gap:10px}
.topbar .socials i{width:7px;height:7px;border-radius:50%;background:#fff;display:block}
.nav{left:0;top:22px;width:1118px;height:54px;background:#fff;border-bottom:1px solid var(--line)}
.brand{left:141px;top:6px;display:flex;align-items:center;gap:7px;z-index:3}
.brand .mark{width:60px;height:60px;border-radius:50%;border:2px solid var(--navy);background:#fff}
.brand .name{font-family:"Anton",sans-serif;font-size:13px;color:var(--navy);line-height:1.1;width:120px}
.menu{left:408px;top:0;height:54px;display:flex;align-items:center;font-size:10.5px;color:var(--ink)}
.menu a{padding:0 12px;border-right:1px solid #bbb;line-height:12px;text-decoration:none;color:inherit}
.menu a:last-child{border-right:none}
.menu .active{position:relative}
.menu .active::before{content:"";position:absolute;left:-3px;top:-3px;width:14px;height:14px;border-radius:50%;background:var(--red);z-index:-1}
.contact-btn{left:876px;top:13px;width:102px;height:28px}

/* hero */
.hero{left:0;top:76px;width:1118px;height:534px;background:linear-gradient(180deg,#2c4f96 0%,#1f4189 45%,#163476 100%)}
.hero-title{position:absolute;left:0;width:1118px;top:118px;text-align:center;color:#fff;font-size:74px;line-height:82px}
.hero-sub{position:absolute;left:0;width:1118px;top:296px;text-align:center;color:#fff;font-size:13.5px;line-height:21px}
.hero .btn{top:416px;height:30px}
.btn.white{background:#fff;color:var(--red)}

/* about */
.about-img1{left:141px;top:692px;width:213px;height:350px;background:linear-gradient(160deg,#8a5a2c,#e0a040 45%,#4a2d16)}
.about-img2{left:368px;top:695px;width:226px;height:368px;background:linear-gradient(170deg,#2b2b2f,#4b4b55 50%,#1c1c22)}
.call-pill{left:173px;top:1010px;width:146px;height:55px;background:var(--red);border-radius:28px;color:#fff;display:flex;align-items:center;gap:9px;padding:0 12px}
.call-pill .ico{width:30px;height:30px;border-radius:50%;background:var(--navy);display:flex;align-items:center;justify-content:center}
.call-pill small{display:block;font-size:8px}
.call-pill b{font-size:11px;font-weight:600}
.about-title{left:630px;top:688px;font-size:38px}
.about-text{left:630px;top:745px;width:348px;font-size:9.5px;line-height:16px;color:var(--muted)}
.quote{left:630px;top:837px;width:348px;height:64px;background:#f6f6f6;border-left:3px solid var(--red);font-size:9.5px;line-height:16px;padding:7px 18px;color:var(--ink)}
.stat{left:630px;top:932px;width:150px;height:66px;border:2px solid var(--red);border-radius:4px;display:flex;align-items:center;justify-content:center;gap:6px}
.stat b{font-family:"Anton",sans-serif;font-size:34px;color:var(--navy);font-weight:400}
.stat span{font-size:9.5px;line-height:12px}
.certs{left:802px;top:936px;display:grid;grid-template-columns:74px 80px;row-gap:14px;font-family:"Anton",sans-serif;font-size:14px;color:var(--navy)}
.certs div{display:flex;align-items:center;gap:6px}
.tick{width:11px;height:11px;border-radius:50%;background:var(--red);display:inline-flex;align-items:center;justify-content:center;flex:none}
.about-btn{left:630px;top:1034px;width:158px}

/* section titles */
.sec-title{position:absolute;left:0;width:1118px;text-align:center;font-size:38px}

/* markets */
.m1{left:141px;top:1227px;width:153px;height:262px;background:linear-gradient(160deg,#8ea3b4,#3f5566 60%,#b6a64a)}
.m2{left:308px;top:1227px;width:335px;height:262px;background:linear-gradient(180deg,#2a74c8 0%,#6aa6e0 40%,#7a5a40 70%,#4a3a2e)}
.m3{left:658px;top:1227px;width:151px;height:262px;background:linear-gradient(180deg,#b9bcc0,#80858a 60%,#5b5f63)}
.m4{left:825px;top:1227px;width:153px;height:262px;background:linear-gradient(180deg,#c9c3b2,#8a6a4a 55%,#4a5a3a)}
.market-card{left:348px;top:1449px;width:255px;height:91px;background:#fff;box-shadow:0 4px 12px rgba(0,0,0,.12);text-align:center;padding:14px 14px}
.market-card h3{font-family:"Anton",sans-serif;font-weight:400;font-size:15px;color:var(--navy);text-transform:uppercase}
.market-card p{font-size:8.5px;line-height:14px;color:var(--muted);margin-top:4px}

/* products */
.products-band{left:0;top:1684px;width:1118px;height:324px;background:linear-gradient(180deg,#0f2f74,#0b2660)}
.card{position:absolute;top:1824px;width:269px;height:301px;background:#fff;border-radius:3px;box-shadow:0 3px 10px rgba(0,0,0,.12)}
.card .img{position:absolute;left:0;top:0;width:269px;height:184px;border-radius:3px 3px 0 0}
.card .badge{position:absolute;left:14px;top:146px;width:56px;height:56px;border-radius:50%;background:var(--red);border:4px solid #fff;display:flex;align-items:center;justify-content:center}
.card h3{position:absolute;left:14px;top:210px;font-size:14.5px;font-weight:600;color:var(--ink)}
.card p{position:absolute;left:14px;top:236px;width:245px;font-size:8.5px;line-height:14px;color:var(--muted)}
.card .more{position:absolute;left:14px;top:278px;font-size:8.5px;font-weight:600}

/* why */
.why{position:absolute;width:200px}
.why svg{display:block;height:40px;width:40px}
.why h4{font-family:"Anton",sans-serif;font-weight:400;font-size:14px;text-transform:uppercase;margin-top:14px;color:var(--ink)}
.why p{font-size:9.5px;line-height:17px;color:var(--muted);margin-top:4px}

/* completed */
.arrow{position:absolute;top:2792px;width:36px;height:36px;border-radius:50%;display:flex;align-items:center;justify-content:center}
.proj{top:2882px;height:299px;border-radius:0}
.proj-label{position:absolute;left:425px;top:3150px;width:269px;height:31px;background:#1a1a1a;color:#fff;font-size:12px;font-weight:500;display:flex;align-items:center;justify-content:center;text-transform:uppercase}

/* experience */
.exp-img{left:155px;top:3256px;width:441px;height:448px;border-radius:18px 3px 3px 3px;background:linear-gradient(180deg,#3f7fd0 0%,#7fb1e6 45%,#a89476 70%,#7a6a52)}
.exp-card{left:538px;top:3290px;width:427px;height:383px;background:#fff;box-shadow:0 4px 18px rgba(0,0,0,.12);padding:32px 36px}
.exp-card h2{font-size:38px}
.exp-list{margin-top:22px;list-style:none}
.exp-list li{display:flex;gap:10px;font-family:"Anton",sans-serif;font-size:14px;color:var(--navy);text-transform:uppercase;line-height:21px;margin-bottom:10px}
.exp-list .tick{margin-top:5px}

/* contact */
.map{left:210px;top:3868px;width:329px;height:315px;background:linear-gradient(135deg,#f4f1ea,#e6e3da 60%,#dfe6ef);border-radius:2px;z-index:2}
.field{position:absolute;left:576px;width:335px;background:var(--field);border-radius:3px;font-size:10px;padding:8px 15px;color:var(--ink);z-index:2}
.footer{left:0;top:4141px;width:1118px;height:466px;background:linear-gradient(180deg,#0f2f74,#0a2257)}
.contact-item{position:absolute;top:4206px;display:flex;gap:10px;align-items:center;color:#fff;z-index:3}
.contact-item b{font-family:"Anton",sans-serif;font-weight:400;font-size:12px;display:block}
.contact-item span{font-size:9.5px}
.submit{left:576px;top:4206px;width:335px;z-index:3}
.foot-brand{left:141px;top:4319px;width:167px;height:167px;border-radius:50%;background:#fff;display:flex;align-items:center;justify-content:center;text-align:center;font-family:"Anton",sans-serif;font-size:17px;line-height:1.15;color:var(--navy);padding:18px}
.foot-col{position:absolute;top:4332px;color:#fff}
.foot-col h5{font-family:"Anton",sans-serif;font-weight:400;font-size:14px;text-transform:uppercase;margin-bottom:14px}
.foot-col a{display:block;color:#dfe5f2;font-size:10px;line-height:27px;text-decoration:none}
.social-row{display:flex;align-items:center;gap:9px;font-size:10px;color:#dfe5f2;line-height:32px}
.social-row i{width:22px;height:22px;border-radius:50%;background:#fff;display:block}
.divider{left:141px;top:4547px;width:837px;height:1px;background:rgba(255,255,255,.3)}
.copy{left:0;width:1118px;top:4565px;text-align:center;color:#dfe5f2;font-size:8.5px}
</style>
</head>
<body>
<div class="page">

  <!-- top bar -->
  <div class="abs topbar">
    <span><svg width="8" height="8" viewBox="0 0 24 24"><path fill="#c8102e" d="M6.6 10.8a15 15 0 006.6 6.6l2.2-2.2c.3-.3.7-.4 1-.2 1.1.4 2.3.6 3.6.6.6 0 1 .4 1 1V20c0 .6-.4 1-1 1A17 17 0 013 4c0-.6.4-1 1-1h3.5c.6 0 1 .4 1 1 0 1.3.2 2.5.6 3.6.1.3 0 .7-.2 1z"/></svg>555-014-2277</span>
    <span><i class="dot"></i>info@ridgelineforgecraftllc.example</span>
    <div class="socials"><i></i><i></i><i></i><i></i></div>
  </div>

  <!-- nav -->
  <div class="abs nav"></div>
  <div class="abs brand"><div class="mark"></div><div class="name">Ridgeline Forgecraft</div></div>
  <nav class="abs menu">
    <a class="active">Home</a><a>About Us</a><a>Markets Served</a><a>Product Solutions</a><a>Experience</a>
  </nav>
  <div class="btn contact-btn">Contact Us</div>

  <!-- hero -->
  <section class="abs hero" role="img" aria-label="Steel frame construction site under a blue sky with a faint flag overlay">
    <h1 class="heading hero-title">Building Strength<br>Precision And Trust</h1>
    <p class="hero-sub">Veteran-Owned Metal Fabrication Firm Delivering Custom, Ornamental, And Architectural Metal<br>Solutions For Commercial Construction Projects.</p>
    <div class="btn" style="left:435px;width:120px">Request A Quote</div>
    <div class="btn white" style="left:578px;width:108px">Get Started</div>
  </section>

  <!-- about -->
  <div class="photo about-img1" role="img" aria-label="Sparks flying from metal grinding"></div>
  <div class="photo about-img2" role="img" aria-label="Welder in protective gear at work"></div>
  <div class="abs call-pill">
    <div class="ico"><svg width="14" height="14" viewBox="0 0 24 24"><path fill="#fff" d="M4 4h16v11H8l-4 4z"/></svg></div>
    <div><small>Call to Questions</small><b>+1 555 0100 8060</b></div>
  </div>
  <h2 class="abs heading red about-title">About Us</h2>
  <p class="abs about-text">Ridgeline Forgecraft &amp; Decorative Steel LLC is a veteran-owned and operated metal fabrication firm with decades of combined experience. We deliver custom, ornamental, and architectural metal solutions designed to meet the demands of commercial construction projects.</p>
  <div class="abs quote">Our Team Specializes In Fabricating And Installing Metal Stairs, Guardrails, Handrails, Railings, Fencing, And Ornamental Metals That Combine Durability, Code.</div>
  <div class="abs stat"><b>30+</b><span>Year Of<br>Experience</span></div>
  <div class="abs certs">
    <div><i class="tick"></i>(VBE)</div><div><i class="tick"></i>(SBE)</div>
    <div><i class="tick"></i>(VFBE)</div><div><i class="tick"></i>(SDVOSB)</div>
  </div>
  <div class="btn about-btn">Discover More About</div>

  <!-- markets -->
  <h2 class="sec-title heading red" style="top:1154px">Markets We Serve</h2>
  <div class="photo m1" role="img" aria-label="Engineer with a laptop inside an industrial plant"></div>
  <div class="photo m2" role="img" aria-label="Commercial building under construction with a red crane"></div>
  <div class="photo m3" role="img" aria-label="Industrial processing facility interior"></div>
  <div class="photo m4" role="img" aria-label="Steel framework beside high-rise towers"></div>
  <div class="abs market-card">
    <h3>Commercial Construction</h3>
    <p>Lorem ipsum dolor sit amet consectetur. Porta justo vulputate quisque egestas blandit risus mattis</p>
  </div>
  <div class="btn" style="left:499px;top:1591px;width:120px">Discover More</div>

  <!-- products -->
  <div class="abs products-band" role="img" aria-label="Dark blue band with a faint construction photo"></div>
  <h2 class="sec-title heading" style="top:1752px;color:#fff">Our Product Solutions</h2>

  <div class="card" style="left:141px">
    <div class="img" role="img" aria-label="Exterior steel staircase with handrails" style="background:linear-gradient(160deg,#8a9a80,#c8ccc8 55%,#6c7a5a)"></div>
    <div class="badge"><svg width="26" height="22" viewBox="0 0 26 22" fill="none" stroke="#fff" stroke-width="2"><path d="M2 4h22M2 4v16M24 4v16M7 4v16M12 4v16M17 4v16M2 20h22"/></svg></div>
    <h3>Handrails &amp; Guardrails</h3>
    <p>Lorem ipsum dolor sit amet consectetur. Porta justo vulputate quisque egestas blandit risus mattis</p>
    <div class="more">READ MORE ›</div>
  </div>
  <div class="card" style="left:425px">
    <div class="img" role="img" aria-label="Elevated steel catwalk against the sky" style="background:linear-gradient(180deg,#8fb6e0,#c4d8ec 55%,#7b8a6a)"></div>
    <div class="badge"><svg width="26" height="22" viewBox="0 0 26 22" fill="none" stroke="#fff" stroke-width="2"><path d="M2 10h22M4 10v10M22 10v10M2 6h22M8 6v4M13 6v4M18 6v4"/></svg></div>
    <h3>Catwalks &amp; Platforms</h3>
    <p>Lorem ipsum dolor sit amet consectetur. Porta justo vulputate quisque egestas blandit risus mattis</p>
    <div class="more">READ MORE ›</div>
  </div>
  <div class="card" style="left:711px">
    <div class="img" role="img" aria-label="Welder fabricating steel in a workshop" style="background:linear-gradient(160deg,#5a6a80,#2e3a4a 60%,#8aa0c0)"></div>
    <div class="badge"><svg width="24" height="24" viewBox="0 0 24 24" fill="none" stroke="#fff" stroke-width="2"><circle cx="12" cy="8" r="5"/><path d="M4 22v-4a8 8 0 0116 0v4"/></svg></div>
    <h3>Custom Metal Fabrication</h3>
    <p>Lorem ipsum dolor sit amet consectetur. Porta justo vulputate quisque egestas blandit risus mattis</p>
    <div class="more">READ MORE ›</div>
  </div>
  <div class="btn" style="left:457px;top:2161px;width:204px">Explore Our Metal Solutions</div>

  <!-- why -->
  <h2 class="sec-title heading red" style="top:2262px">Why Contractors Choose Us</h2>

  <div class="why" style="left:141px;top:2355px">
    <svg viewBox="0 0 40 40" fill="none" stroke="#0d2a6b" stroke-width="2"><circle cx="20" cy="20" r="17"/><path d="M20 9v11l7 5"/></svg>
    <h4>Stay On Schedule</h4><p>We deliver projects on time, meeting even aggressive timelines</p>
  </div>
  <div class="why" style="left:354px;top:2355px">
    <svg viewBox="0 0 40 40" fill="none" stroke="#0d2a6b" stroke-width="2"><rect x="8" y="4" width="24" height="32" rx="4"/><path d="M13 12h14M13 19h14M13 26h9"/></svg>
    <h4>Get The Look You Want</h4><p>From functional handrails to custom ornamental features</p>
  </div>
  <div class="why" style="left:567px;top:2355px">
    <svg viewBox="0 0 40 40" fill="none" stroke="#0d2a6b" stroke-width="2"><rect x="4" y="18" width="22" height="14" rx="2"/><circle cx="15" cy="25" r="3"/><path d="M28 10l8 8-8 8"/></svg>
    <h4>Lower Costs Over Time</h4><p>Durable materials reduce maintenance and extend performance</p>
  </div>
  <div class="why" style="left:780px;top:2355px">
    <svg viewBox="0 0 40 40"><rect x="2" y="8" width="36" height="24" fill="#fff" stroke="#ccc"/><g fill="#c8102e"><rect x="2" y="8" width="36" height="3.4"/><rect x="2" y="14.8" width="36" height="3.4"/><rect x="2" y="21.6" width="36" height="3.4"/><rect x="2" y="28.4" width="36" height="3.6"/></g><rect x="2" y="8" width="16" height="13" fill="#0d2a6b"/></svg>
    <h4>American Made</h4><p>Fabricated with pride in the USA, supporting local industries</p>
  </div>
  <div class="why" style="left:141px;top:2507px">
    <svg viewBox="0 0 40 40" fill="none" stroke="#0d2a6b" stroke-width="2"><circle cx="20" cy="20" r="7"/><circle cx="20" cy="20" r="14" stroke-dasharray="5 4"/></svg>
    <h4>Modern Technology</h4><p>Leveraging advanced tools for precision, efficiency, and quality results</p>
  </div>
  <div class="why" style="left:354px;top:2507px">
    <svg viewBox="0 0 40 40" fill="none" stroke="#0d2a6b" stroke-width="2"><path d="M20 6v28M8 14h24M8 14l-5 10h10zM32 14l-5 10h10zM12 34h16"/></svg>
    <h4>Value Engineering Options</h4><p>Practical solutions to balance cost, performance, and aesthetics</p>
  </div>
  <div class="why" style="left:567px;top:2507px">
    <svg viewBox="0 0 40 40" fill="none" stroke="#0d2a6b" stroke-width="2"><circle cx="20" cy="12" r="5"/><path d="M10 34v-6a10 10 0 0120 0v6M4 6l4 4M36 6l-4 4"/></svg>
    <h4>Confidence Built In</h4><p>Trusted by contractors and developers for dependable delivery</p>
  </div>
  <div class="why" style="left:780px;top:2507px">
    <svg viewBox="0 0 40 40" fill="none" stroke="#0d2a6b" stroke-width="2"><path d="M2 18l8-6 8 4 6-4 14 8M10 12l-6 12 10 8 4-2M38 20l-8 10-6-2"/></svg>
    <h4>Achieve Inclusion Goals</h4><p>Partnering with a certified SBE, VBE, SDVOSB, VFBE, and MBE-ready firm helps meet diversity participation requirements</p>
  </div>
  <div class="btn" style="left:476px;top:2686px;width:166px">Partner With Us Today</div>

  <!-- completed -->
  <h2 class="abs heading red" style="left:141px;top:2792px;font-size:38px">Completed Project</h2>
  <div class="arrow" style="left:916px;background:#ececec"><svg width="14" height="10" viewBox="0 0 14 10" fill="none" stroke="#333" stroke-width="1.6"><path d="M13 5H1M5 1L1 5l4 4"/></svg></div>
  <div class="arrow" style="left:960px;background:var(--navy)"><svg width="14" height="10" viewBox="0 0 14 10" fill="none" stroke="#fff" stroke-width="1.6"><path d="M1 5h12M9 1l4 4-4 4"/></svg></div>
  <div class="photo proj" style="left:0;width:124px;background:linear-gradient(160deg,#6f8aa6,#a7b6c6)" role="img" aria-label="Steel stair inside a warehouse"></div>
  <div class="photo proj" style="left:141px;width:269px;background:linear-gradient(180deg,#cfd3d6,#8f969c 60%,#5a5f63)" role="img" aria-label="Long industrial hall with steel trusses"></div>
  <div class="photo proj" style="left:425px;width:269px;background:linear-gradient(180deg,#d6d6d6,#a9a9a9 60%,#e9e9e9)" role="img" aria-label="Empty warehouse with polished floor"></div>
  <div class="proj-label">Project Name 1</div>
  <div class="photo proj" style="left:711px;width:270px;background:linear-gradient(180deg,#2f6fc6,#7fb0e6 55%,#6a7482)" role="img" aria-label="Blue steel frame structure against the sky"></div>
  <div class="photo proj" style="left:994px;width:124px;background:linear-gradient(180deg,#e4e7ea,#b9bec3)" role="img" aria-label="Bright warehouse interior"></div>

  <!-- experience -->
  <div class="photo exp-img" role="img" aria-label="Open steel structure frame on a dirt site"></div>
  <div class="abs exp-card">
    <h2 class="heading red">Experience Snapshot</h2>
    <ul class="exp-list">
      <li><i class="tick"></i>Decades Of Combined Fabrication Experience</li>
      <li><i class="tick"></i>Proven Track Record With Fortune 500 Manufacturers</li>
      <li><i class="tick"></i>Government, Commercial, And Industrial Project Execution Expertise</li>
      <li><i class="tick"></i>On-Time, Precision-Built Projects Nationwide</li>
    </ul>
    <div class="btn" style="left:36px;top:329px;width:150px">Start Your Project</div>
  </div>

  <!-- contact -->
  <h2 class="sec-title heading red" style="top:3780px">Get In Touch With Us</h2>
  <div class="abs footer" role="img" aria-label="Navy band with a faint flag texture"></div>
  <div class="abs map" role="img" aria-label="Street map showing the office location"></div>
  <div class="field" style="top:3869px;height:33px">Name</div>
  <div class="field" style="top:3919px;height:33px">Mobile Phone</div>
  <div class="field" style="top:3969px;height:33px">Email</div>
  <div class="field" style="top:4017px;height:162px">Message</div>

  <div class="contact-item" style="left:210px">
    <svg width="34" height="34" viewBox="0 0 34 34" fill="none" stroke="#fff" stroke-width="1.6"><rect x="3" y="8" width="28" height="20" rx="2"/><path d="M3 9l14 10 14-10"/></svg>
    <div><b>EMAIL US</b><span>info@ridgelineforgecraftllc.example</span></div>
  </div>
  <div class="contact-item" style="left:432px">
    <svg width="34" height="34" viewBox="0 0 24 24" fill="none" stroke="#fff" stroke-width="1.2"><path d="M6.6 10.8a15 15 0 006.6 6.6l2.2-2.2c.3-.3.7-.4 1-.2 1.1.4 2.3.6 3.6.6.6 0 1 .4 1 1V20c0 .6-.4 1-1 1A17 17 0 013 4c0-.6.4-1 1-1h3.5c.6 0 1 .4 1 1 0 1.3.2 2.5.6 3.6.1.3 0 .7-.2 1z"/></svg>
    <div><b>PHONE</b><span>555-014-2277</span></div>
  </div>
  <div class="btn submit">Submit Now</div>

  <!-- footer -->
  <div class="abs foot-brand">Ridgeline Forgecraft</div>
  <div class="foot-col" style="left:483px">
    <h5>Quick Links</h5>
    <a>Home</a><a>About Us</a><a>Markets Served</a><a>Product Solutions</a><a>Experience</a>
  </div>
  <div class="foot-col" style="left:663px">
    <h5>Product Solution</h5>
    <a>Handrails &amp; Guardrails</a><a>Catwalks &amp; Platforms</a><a>Custom Metal Fabrication</a><a>Decorative Metal Railings</a><a>Decorative Glazed Railings</a>
  </div>
  <div class="foot-col" style="left:893px">
    <h5>Follow Us</h5>
    <div class="social-row"><i></i>Friendspace</div>
    <div class="social-row"><i></i>Chirpline</div>
    <div class="social-row"><i></i>Snapgrid</div>
    <div class="social-row"><i></i>Streamcast</div>
  </div>
  <div class="abs divider"></div>
  <p class="abs copy">Copyright 2025 . All Rights Reserved</p>

</div>
</body>
</html>
```